Webdesign für Physiotherapie
Zielgruppe
Physiotherapie unter ganzheitlichen oder umfangreicheren Gesichtspunkten.
ANLAGE BEACHTEN!
Aufgabenstellung
Siehe Anlage!

```html
<!DOCTYPE html>
<html lang="de">
<head>
<meta charset="utf-8">
<title>Jonas Berghof – Privatpraxis für Physiotherapie</title>
<link href="https://fonts.googleapis.com/css2?family=Roboto:wght@400;500;700&display=swap" rel="stylesheet">
<style>
  :root {
    --red: #e5432a;
    --gold: #d8ad2a;
    --ink: #111111;
    --dark: #1d1d1d;
    --grey: #d6d6d6;
    --white: #ffffff;
  }
  * { box-sizing: border-box; margin: 0; padding: 0; }
  html, body { width: 1200px; height: 3689px; overflow: hidden; }
  body { position: relative; background: var(--white); color: var(--ink); font-family: "Roboto", sans-serif; }
  .abs { position: absolute; }

  .brand { left: 0; width: 1200px; text-align: center; color: var(--gold); font-family: "Roboto", sans-serif; font-weight: 700; }
  .brand-name { font-size: 32px; letter-spacing: 1px; display: inline-flex; align-items: center; gap: 14px; }
  .brand-dot { width: 22px; height: 22px; border-radius: 50%; background: var(--gold); display: inline-block; }
  .brand-tag { font-size: 13px; letter-spacing: 1.5px; margin-top: 8px; }

  .photo { background: linear-gradient(135deg, #8a8a8a, #d0d0d0); }
  .hero { left: 16px; top: 286px; width: 1184px; height: 440px;
    background: linear-gradient(100deg, #9c9a92 0%, #4b4a40 30%, #8d6b55 55%, #e6d6cf 80%, #f0e7e2 100%); }
  .hero-title { right: 66px; top: 420px; text-align: right; font-weight: 500; font-size: 52px; line-height: 60px; }
  .btn { background: var(--red); color: var(--white); border-radius: 30px; font-weight: 500; display: flex; align-items: center; justify-content: center; }
  .hero-btn { left: 1040px; top: 548px; width: 94px; height: 38px; font-size: 18px; }

  .stats { left: 192px; top: 637px; width: 811px; height: 181px; background: var(--dark); border-radius: 58px; display: flex; color: var(--white); overflow: hidden; }
  .stat { flex: 1; padding: 28px 30px 0 66px; }
  .stat + .stat { border-left: 2px solid #f2f2f2; }
  .stat:nth-child(2) { text-align: center; padding: 28px 30px 0; }
  .stat:nth-child(3) { text-align: right; padding: 28px 70px 0 30px; }
  .stat h3 { font-size: 26px; font-weight: 500; margin-bottom: 16px; }
  .stat:nth-child(1) h3 { padding-left: 0; }
  .stat p { font-size: 13px; line-height: 17px; }

  .about-img { left: 24px; top: 898px; width: 486px; height: 521px; border-radius: 243px 243px 0 0;
    background: linear-gradient(160deg, #3a3a3a, #9a9a9a 50%, #d9d9d9); }
  .h2 { font-weight: 500; font-size: 40px; line-height: 50px; }
  .body { font-size: 18.5px; line-height: 24px; }
  .about-title { left: 534px; top: 956px; width: 620px; }
  .about-text { left: 534px; top: 1148px; width: 640px; }
  .btn-outline { left: 534px; top: 1346px; width: 95px; height: 36px; border: 2px solid var(--red); border-radius: 20px; color: var(--red); font-weight: 500; font-size: 18px; display: flex; align-items: center; justify-content: center; }

  .band { left: 0; width: 1197px; height: 18px; background: var(--red); }
  .grey { left: 0; width: 1200px; background: var(--grey); }
  .sec-title { left: 46px; }
  .sec-text { left: 46px; width: 550px; }

  .circle { border-radius: 50%; border: 8px solid var(--dark); }
  .circle.red { border-color: var(--red); }

  .fasz-img { left: 46px; top: 1929px; width: 315px; height: 308px; border: 11px solid var(--red); border-radius: 36px;
    background: linear-gradient(180deg, #0e1626, #2b3f55 55%, #6aa1b5); }

  .contact-title { left: 47px; top: 2816px; font-size: 52px; font-weight: 700; }
  .field { left: 47px; width: 550px; font-size: 24px; border-bottom: 1.5px solid var(--ink); }
  .label { left: 49px; font-size: 24px; }
  .send { left: 49px; top: 3196px; width: 144px; height: 45px; font-size: 25px; font-weight: 400; }
  .contact-img { left: 670px; top: 2771px; width: 487px; height: 520px; border-radius: 0 0 243px 243px;
    background: linear-gradient(200deg, #5a5a5a, #cfcfcf 45%, #8a8a8a 75%, #2a2a2a); }
</style>
</head>
<body>

<header class="brand abs" style="top:192px;">
  <div class="brand-name"><span class="brand-dot"></span>JONAS BERGHOF</div>
  <div class="brand-tag">Privatpraxis für Physiotherapie</div>
</header>

<section>
  <div class="hero abs" role="img" aria-label="Foto: Therapeut legt die Hand auf die Schulter eines Patienten"></div>
  <h1 class="hero-title abs h2" style="font-size:52px;line-height:60px;">Qualifizierter<br>Physiotherapeut.</h1>
  <div class="btn hero-btn abs">Kontakt</div>

  <div class="stats abs">
    <div class="stat"><h3>Erfahrung</h3><p>Lorem Ipsum dolor sit amet.Lorem Ipsum dolor sit amet.Lorem Ipsum dolor sit amet.</p></div>
    <div class="stat"><h3>Kunden</h3><p>Lorem Ipsum dolor sit amet.Lorem Ipsum dolor sit amet.Lorem Ipsum dolor sit amet.</p></div>
    <div class="stat"><h3>Mitarbeiter</h3><p>Lorem Ipsum dolor sit amet.Lorem Ipsum dolor sit amet.Lorem Ipsum dolor sit amet.</p></div>
  </div>
</section>

<section>
  <div class="about-img abs" role="img" aria-label="Schwarzweißfoto: Trainierende Person im Ausfallschritt mit gefalteten Händen"></div>
  <h2 class="about-title abs h2">Ihr Ansprechpartner für Physiotherapeutische Behandlung</h2>
  <p class="about-text abs body">Yorem ipsum dolor sit amet, consectetur adipiscing elit. Nunc vulputate libero et velit interdum, ac aliquet odio mattis. Class aptent taciti sociosqu ad litora torquent per conubia nostra, per inceptos himenaeos. Yorem ipsum dolor sit amet, consectetur adipiscing elit. Nunc vulputate libero et velit interdum, ac aliquet odio mattis. Class aptent taciti sociosqu ad litora torquent per conubia nostra, per inceptos sociosqu ad litora torquent per conubia nostra, per inceptos himenaeos.</p>
  <div class="btn-outline abs">Kontakt</div>
</section>

<div class="band abs" style="top:1419px;"></div>

<section>
  <div class="grey abs" style="top:1494px;height:363px;"></div>
  <h2 class="sec-title abs h2" style="top:1514px;">energetische<br>Betrachtungsweise</h2>
  <p class="sec-text abs body" style="top:1634px;">Yorem ipsum dolor sit amet, consectetur adipiscing elit. Nunc vulputate libero et velit interdum, ac aliquet odio mattis. Class aptent taciti sociosqu ad litora torquent per conubia nostra, per inceptos himenaeos. Yorem ipsum dolor sit amet, consectetur adipiscing elit. Nunc vulputate libero et velit interdum, ac aliquet odio mattis. Class aptent taciti sociosqu ad litora torquent per conubia nostra, per inceptos sociosqu ad litora torquent per conubia nostra, per inceptos himenaeos.</p>
  <div class="circle red abs photo" style="left:698px;top:1489px;width:330px;height:330px;background:linear-gradient(150deg,#e8e8e8,#9aa0a8 55%,#3a3f48);" role="img" aria-label="Foto: Therapeut behandelt die Hand eines Patienten am Arbeitstisch"></div>
  <div class="circle abs photo" style="left:646px;top:1458px;width:186px;height:186px;background:linear-gradient(160deg,#f2f2f2,#c9c9c9 60%,#6d6d6d);" role="img" aria-label="Foto: Hände mit kleiner Übungshantel"></div>
  <div class="circle abs photo" style="left:892px;top:1689px;width:180px;height:180px;background:linear-gradient(170deg,#f4f4f4,#cfcfcf 50%,#2b3246);" role="img" aria-label="Foto: Person hält eine Faszienrolle hinter dem Rücken"></div>
</section>

<section>
  <div class="fasz-img abs" role="img" aria-label="Foto: Frau dehnt sich rücklings über einem Gymnastikball"></div>
  <h2 class="abs h2" style="left:414px;top:1930px;">fasziale-funktionelle<br>Betrachtungsweise</h2>
  <p class="abs body" style="left:414px;top:2064px;width:680px;">Yorem ipsum dolor sit amet, consectetur adipiscing elit. Nunc vulputate libero et velit interdum, ac aliquet odio mattis. Class aptent taciti sociosqu ad litora torquent per conubia nostra, per inceptos himenaeos. Yorem ipsum dolor sit amet, consectetur adipiscing elit. Nunc vulputate libero et velit interdum, ac aliquet odio mattis. Class aptent taciti sociosqu ad litora torquent per conubia nostra, per inceptos sociosqu ad litora torquent per conubia nostra, per inceptos himenaeos.</p>
</section>

<section>
  <div class="grey abs" style="top:2310px;height:382px;"></div>
  <h2 class="sec-title abs h2" style="top:2319px;">axiale<br>Betrachtungsweise</h2>
  <p class="sec-text abs body" style="top:2442px;">Yorem ipsum dolor sit amet, consectetur adipiscing elit. Nunc vulputate libero et velit interdum, ac aliquet odio mattis. Class aptent taciti sociosqu ad litora torquent per conubia nostra, per inceptos himenaeos. Yorem ipsum dolor sit amet, consectetur adipiscing elit. Nunc vulputate libero et velit interdum, ac aliquet odio mattis. Class aptent taciti sociosqu ad litora torquent per conubia nostra, per inceptos sociosqu ad litora torquent per conubia nostra, per inceptos himenaeos.</p>
  <div class="circle red abs photo" style="left:694px;top:2327px;width:330px;height:330px;background:linear-gradient(150deg,#e8e8e8,#9aa0a8 55%,#3a3f48);" role="img" aria-label="Foto: Therapeut behandelt die Hand eines Patienten am Arbeitstisch"></div>
  <div class="circle abs photo" style="left:895px;top:2299px;width:180px;height:180px;background:linear-gradient(160deg,#f2f2f2,#c9c9c9 60%,#6d6d6d);" role="img" aria-label="Foto: Hände mit kleiner Übungshantel"></div>
  <div class="circle abs photo" style="left:652px;top:2525px;width:180px;height:180px;background:linear-gradient(170deg,#f4f4f4,#cfcfcf 50%,#2b3246);" role="img" aria-label="Foto: Person hält eine Faszienrolle hinter dem Rücken"></div>
</section>

<div class="band abs" style="top:2750px;"></div>

<section>
  <h2 class="contact-title abs">Kontakt</h2>
  <div class="label abs" style="top:2899px;">Name</div>
  <div class="field abs" style="top:2926px;"></div>
  <div class="label abs" style="top:2964px;">E-Mail</div>
  <div class="field abs" style="top:2993px;"></div>
  <div class="label abs" style="top:3019px;">Nachricht</div>
  <div class="field abs" style="top:3175px;"></div>
  <div class="btn send abs">Absenden</div>
  <div class="contact-img abs" role="img" aria-label="Schwarzweißfoto: Therapeut hält und streckt das Handgelenk einer Person"></div>
</section>

<footer class="brand abs" style="top:3595px;">
  <div class="brand-name"><span class="brand-dot"></span>JONAS BERGHOF</div>
  <div class="brand-tag">Privatpraxis für Physiotherapie</div>
</footer>

</body>
</html>
```